Webdesign für Raumgestalter / Interior Designer und Implementierung
Zielgruppe
Wir möchten zukünftig für Menschen «Träume in Räume» verwandeln und sind spezialisiert auf Interior Design, ReDesign Home Staging wie auch Dekorationen mit folgenden Leistungen an:
- Interior Design
- Home Styling
- Home Staging
- Dekoration
Aufgabenstellung
(Wichtig: Bitte Anforderungen und Fotos im PDF File im Anhang beachten)
Aufbau der Homepage
Homepage wird in verschiedenen Seiten/Fenster aufgebaut. Diese können oben auf der Homepage angeklickt werden. Der Aufbau ist in 5 Seiten: Home, Leistungen, Referenzen, Pakete und Preise, Kontakt
- Die Homepage sollte dann von uns gemanagt werden können. (Bspw. Plattformen oder andere Gremien, wo die Homepage einfach und ohne tiefe Informatikkenntnisse gemanagt werden kann :-).)
- Die Leistungen betreffen Templating inkl. Umsetzung (Online-Fertigstellung), ich kann bei der URL-Verknüpfung unterstützen.
1) Home
Willkommensseite, inspirierend, einladend, sollte die Besucher dazu animieren vertiefter die Detail anzuschauen.
Es soll ein Button unten ermöglichen, ins zweite Fenster «Referenzen» zu klicken. Siehe unteres Kapitel.
2) Leistungen
a. Interior Design
b. Home Styling
c. Home Staging
d. Dekoration
Hier wird der Ablauf von Projekten aufgezeigt, dieser bildet sich in:
- Planung, Designen, Realisieren
Weiterer sollen realisierte Design-Projekte von bspw. Räumen mit Fotos aufgeführt sein.
3) Referenzen
- Dieses Fenster soll das Interesse möglicher Kunden im Detail erwecken
- Es soll ein erster Termin telefonisch oder per Videocall stattfinden können
(dient zum Kennenlernen, Bedürfnisse verstehen, Ablauf aufzeigen)
4) Pakete und Preise
Hier werden die Pakete und Preise beschrieben.
Die Preise werden auf Rapportsbasis erstellt und richten sich nach Offerten und Wünschen des Kunden. Preis ist bei 80 Franken pro Stunde, das erste Beratungsgespräch wird nicht verrechnet.
Hier können Details in einer Tabelle / Preisliste erarbeitet werden:
- Private Wohnräume
o Private Wohnung
o Privates Haus
o Ferienimmobilien
- Business Einrichtungen
o Einrichtungen von Geschäften
o NestoFlat-Einrichtungen
o ReDesign für Verkauf von Immo..

```html
<!DOCTYPE html>
<html lang="de">
<head>
<meta charset="utf-8">
<title>Raumfein – Kontakt</title>
<link href="https://fonts.googleapis.com/css2?family=Poppins:wght@500;600&family=Roboto:wght@400;500;700&display=swap" rel="stylesheet">
<style>
  :root {
    --header-bg: #3d3d3d;
    --footer-bg: #383838;
    --section-grey: #b8b8b8;
    --white: #ffffff;
    --ink: #222222;
    --text: #333333;
    --muted: #a8a8a8;
    --field-border: #c9c9c9;
    --button-grey: #b3b3b3;
    --black: #000000;
    --photo-dark: #2b3527;
    --photo-mid: #4d5a44;
    --photo-light: #cfc6b8;
    --brand-teal: #0c6b78;
  }
  * { box-sizing: border-box; margin: 0; padding: 0; }
  html, body { width: 961px; height: 1200px; overflow: hidden; }
  body {
    position: relative;
    background: var(--white);
    font-family: "Roboto", Arial, sans-serif;
    color: var(--text);
  }

  /* Header */
  .site-header {
    position: absolute; left: 0; top: 0; width: 961px; height: 73px;
    background: var(--header-bg);
  }
  .brand {
    position: absolute; left: 22px; top: 15px; width: 71px; height: 43px;
    background: var(--white);
    display: flex; align-items: center; justify-content: center;
    font-family: "Roboto", Arial, sans-serif; font-size: 9px; font-weight: 500;
    letter-spacing: 1px; color: #555555;
  }
  .main-nav a {
    position: absolute; top: 31px; font-size: 9.5px; color: var(--white);
    text-decoration: none; white-space: nowrap;
  }
  .main-nav a.is-active { border-bottom: 1px solid var(--white); padding-bottom: 1px; }
  .header-cta {
    position: absolute; left: 856px; top: 26px; width: 65px; height: 21px;
    background: var(--button-grey); border: 1px solid #d0d0d0; border-radius: 3px;
    color: var(--white); font-size: 9.5px;
    display: flex; align-items: center; justify-content: center;
  }

  /* About */
  .about-photo {
    position: absolute; left: 102px; top: 118px; width: 365px; height: 280px;
    background: radial-gradient(ellipse at 50% 30%, var(--photo-light) 0%, var(--photo-mid) 45%, var(--photo-dark) 100%);
  }
  .about-text { position: absolute; left: 527px; top: 118px; width: 328px; }
  .section-title {
    font-family: "Poppins", Arial, sans-serif; font-weight: 500;
    font-size: 21px; color: var(--ink); line-height: 1.3;
  }
  .about-text .section-title { margin-bottom: 10px; }
  .about-text p { font-size: 9.6px; line-height: 15.8px; margin-bottom: 15.8px; color: var(--text); }

  /* Contact */
  .contact-band {
    position: absolute; left: 0; top: 455px; width: 961px; height: 506px;
    background: var(--section-grey);
  }
  .contact-card {
    position: absolute; left: 102px; top: 494px; width: 747px; height: 433px;
    background: var(--white);
  }
  .contact-card .section-title { position: absolute; left: 17px; top: 20px; }
  .field-label { position: absolute; left: 17px; font-size: 9.6px; color: var(--ink); }
  .field-label .required { color: var(--muted); font-size: 7.5px; }
  .field {
    position: absolute; left: 17px; width: 713px;
    border: 1px solid var(--field-border); border-radius: 3px; background: var(--white);
  }
  .consent {
    position: absolute; left: 17px; top: 331px;
    display: flex; align-items: center; gap: 9px; font-size: 9.6px; color: var(--ink);
  }
  .consent .box { width: 12px; height: 12px; border: 1px solid #8a8a8a; border-radius: 2px; }
  .consent .link { text-decoration: underline; }
  .consent .required { color: var(--muted); font-size: 7.5px; }
  .submit {
    position: absolute; left: 17px; top: 371px; width: 76px; height: 28px;
    background: var(--black); color: var(--white); border-radius: 2px; font-size: 9.5px;
    display: flex; align-items: center; justify-content: center;
  }

  /* Footer */
  .site-footer {
    position: absolute; left: 0; top: 961px; width: 961px; height: 146px;
    background: var(--footer-bg); color: var(--white); font-size: 9.5px; text-align: center;
  }
  .footer-contact { position: absolute; top: 47px; width: 100%; }
  .footer-contact .sep { margin: 0 7px; }
  .footer-links { position: absolute; top: 97px; width: 100%; }
  .footer-links a { color: var(--white); text-decoration: underline; margin: 0 5px; }
  .platform-note {
    position: absolute; left: 0; top: 1142px; width: 961px; text-align: center;
    font-size: 8.5px; color: var(--ink);
  }
  .platform-note .platform-name {
    font-weight: 700; color: var(--brand-teal); margin-right: 6px; font-size: 10px;
  }
  .platform-note .url { text-decoration: underline; }
</style>
</head>
<body>

<header class="site-header">
  <div class="brand">RAUMFEIN</div>
  <nav class="main-nav">
    <a href="#" style="left:318px">Home</a>
    <a href="#" style="left:365px">Leistungen</a>
    <a href="#" style="left:432px">Referenzen</a>
    <a href="#" style="left:500px">Pakete und Preise</a>
    <a href="#" class="is-active" style="left:595px">Kontakt</a>
  </nav>
  <div class="header-cta">Kontakt</div>
</header>

<section class="about">
  <div class="about-photo" role="img" aria-label="Porträt der Dekorateurin in weissem Oberteil zwischen grünen Pflanzen"></div>
  <div class="about-text">
    <h2 class="section-title">Über mich</h2>
    <p>Ich heisse Livia Marković, bin 26 Jahre alt und wohne im Kanton Luzern.</p>
    <p>Ich habe Fashion Design studiert und auch eine Weiterbildung im Visual Merchandising in Luzern erfolgreich abgeschlossen. Zur Zeit arbeite ich als Dekorateurin und habe mehrere Jahre Erfahrung in Dekoration, Visual Merchandising und Design.</p>
    <p>Mein Hobby ist es, neue Designs und Dekorationen für Menschen zu planen, auf Bildwerk Studio zu designen und zu realisieren.</p>
    <p>Mich macht es glücklich, wenn ich meine Kunden glücklich sehe. Ich helfe Ihnen somit von der Ideenfindung, Konzeption bis hin zur Umsetzung Ihrer persönlichen Dekorationen.</p>
  </div>
</section>

<section class="contact-band">
</section>
<div class="contact-card">
  <h2 class="section-title">Kontaktieren Sie mich</h2>
  <div class="field-label" style="top:85px">Name</div>
  <div class="field" style="top:104px;height:28px"></div>
  <div class="field-label" style="top:148px">E-Mail-Adresse <span class="required">(Pflichtfeld)</span></div>
  <div class="field" style="top:167px;height:28px"></div>
  <div class="field-label" style="top:211px">Nachricht</div>
  <div class="field" style="top:231px;height:83px"></div>
  <div class="consent">
    <span class="box"></span>
    <span>Ich habe die <span class="link">Datenschutzerklärung</span> zur Kenntnis genommen und erkläre mich damit einverstanden. <span class="required">(Pflichtfeld)</span></span>
  </div>
  <div class="submit">Absenden</div>
</div>

<footer class="site-footer">
  <div class="footer-contact">
    <span style="text-decoration:underline">livia@raumfein-studio.ch</span><span class="sep">-</span>078 412 56 90<span class="sep">-</span>Birkenhof 7, 6099 Musterwil
  </div>
  <div class="footer-links">
    <a href="#">Impressum</a><a href="#">Datenschutz</a><a href="#">Cookie-Einstellungen</a>
  </div>
</footer>

<div class="platform-note">
  <span class="platform-name">SEITENWERK</span>Das kannst du auch! Melde dich kostenlos an bei <span class="url">https://seitenwerk.example/</span>
</div>

</body>
</html>
```